Harlow Street Players Poster, Flyer, & Corflute Design

Technical requirements: We need designs for an A3 sized poster, a trifold double side A4 sized flyer, and a standard corflute, to advertise our open day, on the .27th of February, 2016 at 12 Dunmore Rd, Watson, ACT. Dates must be in the Australian format: dd/mm/yy or dd/mm/yyyy.
The date sections on all of the designs must be editable, and the flyer must have large sections of content which are easily editable. The flyer must have the room to talk about the history of the organisation, its current size and structure, current programmes, how to join, etc.
All can be full colour.
Artistic requirements: The designs must incorporate our logo (attached), the organisational colours (gold, white, and navy blue), and must achieve three goals. They must:
- Portray the organisation as a fun, diverse, and exciting community of musicians;
- Encourage people to come and participate in our open day and eventually join the organisation.
- Reflect the diverse styles of music the organisation plays, and make jazz and classical music attractive.
Design guidelines:
Ideally the designs should be simple, uncluttered and beautiful. They should focus on conveying information.. They should showcase the band's colours and draw on classic images and designs from jazz and concert band history. They should be eye catching.
Organisational background:
Harlow Street Players was established in 1925 and has a long standing history as the band of Canberra.
HSP supports a variety of ensembles including:
1. Fledgling Wind Group for beginner students.
2. Rising Reed Group for young musicians eager to push their skills to a higher level.
3. Peter Lomond Group, a recreational concert band for those new to an instrument or returning after an absence.
4. Halcyon Swing Crew - a semi-professional big band.
5. Harlow Street Players - A-grade wind ensemble recently runner up at the Federal Brass Trophy Series in Sydney
6. The Ardley Reeds & Horns - flexible, professional chamber wind and brass ensembles.
Regardless of your level, we want to hear from you as Harlow Street Players is always keen to take on new players. We play for a variety of community events throughout the year and if you don't want to play, come have a listen!

```html
<!DOCTYPE html>
<html lang="en">
<head>
<meta charset="utf-8">
<title>Alternative Jazz Concert – Harlow Street Players</title>
<link rel="stylesheet" href="https://fonts.googleapis.com/css2?family=Bebas+Neue&family=Fredoka:wght@600&family=Oswald:wght@500;600&family=Roboto+Condensed:wght@700&display=swap">
<style>
  :root {
    --navy: #1f4c9c;
    --navy-deep: #173a7a;
    --gold: #c99a2e;
    --gold-light: #e0b548;
    --yellow: #f2e62a;
    --white: #ffffff;
    --ink: #1c2b4a;
  }
  * { margin: 0; padding: 0; box-sizing: border-box; }
  html, body { width: 847px; height: 1200px; overflow: hidden; background: var(--white); }
  .poster {
    position: relative; width: 847px; height: 1200px; overflow: hidden;
    background: var(--navy); color: var(--white);
    font-family: "Bebas Neue", "Oswald", sans-serif;
  }
  .gold-panel {
    position: absolute; left: 563px; top: 0; width: 284px; height: 600px;
    background: linear-gradient(90deg, var(--gold) 0%, var(--gold-light) 55%, var(--gold) 100%);
  }
  .festival-tag {
    position: absolute; left: 582px; top: 14px; width: 180px;
    font-size: 42px; line-height: 0.92; color: var(--white); letter-spacing: 0.5px;
  }
  .guitar-art {
    position: absolute; left: 470px; top: 190px; width: 370px; height: 640px;
    border-radius: 160px 160px 180px 180px;
    background: radial-gradient(ellipse at 40% 75%, #2d63c4 0%, #1d4fa8 45%, rgba(230,235,245,0.55) 75%, rgba(31,76,156,0) 100%);
  }
  .headline-kicker { position: absolute; left: 22px; top: 30px; font-size: 40px; line-height: 1; letter-spacing: 1px; }
  .headline-sub { position: absolute; left: 22px; top: 74px; font-size: 32px; letter-spacing: 1px; }
  .headline-jazz {
    position: absolute; left: 18px; top: 104px;
    font-family: "Fredoka", sans-serif; font-weight: 600;
    font-size: 150px; line-height: 1; color: var(--yellow); letter-spacing: 2px;
  }
  .headline-concert { position: absolute; left: 22px; top: 282px; font-size: 70px; letter-spacing: 12px; line-height: 1; }
  .tagline {
    position: absolute; left: 22px; top: 352px;
    font-family: "Roboto Condensed", sans-serif; font-weight: 700; font-size: 22px; color: var(--yellow);
  }
  .venue { position: absolute; left: 22px; top: 398px; font-size: 78px; line-height: 0.92; letter-spacing: 3px; }
  .date-row { position: absolute; left: 22px; top: 545px; display: flex; align-items: center; gap: 14px; }
  .date { font-size: 80px; line-height: 1; letter-spacing: 3px; font-family: "Oswald", sans-serif; font-weight: 500; }
  .date-divider { width: 4px; height: 74px; background: var(--white); }
  .doors {
    font-family: "Roboto Condensed", sans-serif; font-weight: 700;
    font-size: 22px; line-height: 1.1; color: var(--yellow);
  }
  .tickets {
    position: absolute; left: 22px; top: 632px;
    font-family: "Roboto Condensed", sans-serif; font-weight: 700; font-size: 17px;
  }
  .invitation {
    position: absolute; left: 22px; top: 664px; width: 680px;
    font-family: "Oswald", sans-serif; font-weight: 600; font-size: 19px; line-height: 1.18;
    text-transform: uppercase; letter-spacing: 0.3px;
  }
  .invitation .highlight { color: var(--yellow); }
  .background-note {
    position: absolute; left: 0; top: 1036px; width: 847px; text-align: center;
    font-family: "Oswald", sans-serif; font-weight: 600; font-size: 16px; line-height: 1.22; text-transform: uppercase;
  }
  .background-note .label { color: var(--yellow); }
  .footer-strip {
    position: absolute; left: 0; top: 1118px; width: 847px; height: 82px;
    background: var(--white); display: flex; align-items: center; justify-content: space-between; padding: 0 24px;
  }
  .band-mark { display: flex; align-items: center; gap: 14px; }
  .band-mark .dot { width: 46px; height: 46px; border-radius: 50%; background: var(--navy-deep); }
  .band-mark .name { font-family: "Bebas Neue", sans-serif; font-size: 36px; color: var(--navy-deep); letter-spacing: 1px; }
  .supporters { position: relative; display: flex; align-items: flex-end; gap: 12px; padding-top: 14px; }
  .supporters .caption {
    position: absolute; top: 0; right: 0;
    font-family: "Roboto Condensed", sans-serif; font-weight: 700; font-size: 10px; color: var(--ink);
  }
  .badge { background: var(--navy); }
  .badge.round { width: 46px; height: 46px; border-radius: 50%; }
  .badge.wide { width: 80px; height: 40px; }
  .badge.square { width: 52px; height: 40px; background: #9aa8c4; }
</style>
</head>
<body>
<main class="poster">
  <div class="gold-panel"></div>
  <div class="festival-tag">Classical and Jazz Music Festival</div>
  <div class="guitar-art" role="img" aria-label="Illustration of a blue electric guitar"></div>

  <h1>
    <span class="headline-kicker">Canbera Music Festival:</span>
    <span class="headline-sub">Alternative</span>
    <span class="headline-jazz">JAZZ</span>
    <span class="headline-concert">CONCERT</span>
  </h1>
  <p class="tagline">A one-day festival of pure classical sounds</p>
  <p class="venue">12 Dunmore Rd,<br>Watson, ACT.</p>
  <div class="date-row">
    <span class="date">27.02.16</span>
    <span class="date-divider"></span>
    <span class="doors">doors open<br>from 3<br>to 11 pm</span>
  </div>
  <p class="tickets">tickets almost sold out! buy yours and save the date</p>
  <p class="invitation">Regardless of your level, we want to hear from you as Harlow Street Players is always keen to take on new players. We play for a variety of community events throughout the year and if <span class="highlight">you don't want to play, come have a listen!</span></p>

  <p class="background-note"><span class="label">Organisational background:</span><br>Harlow Street Players was established in 1925<br>and has a long standing history as the band of Canberra.</p>

  <footer class="footer-strip">
    <div class="band-mark"><span class="dot"></span><span class="name">Harlow Street Players</span></div>
    <div class="supporters">
      <span class="caption">Supported by</span>
      <span class="badge round"></span>
      <span class="badge wide"></span>
      <span class="badge square"></span>
    </div>
  </footer>
</main>
</body>
</html>
```